WEB SITE BRIEF – “STILL MEADOW ENERGY HEALING”
Registration
• The business has been registered as: “Still Meadow Energy Healing.”
• The web site has been registered as: www.stillmeadow.com.au

About Still Meadow Energy Healing
This is a small company that will be performing fully clothed treatments / healings for clients who may have injuries; sickness; stress in life; looking to relax; enegy balance and spiritual help.

Look and Feel

• Green pallet – that aligns to the logo design;
• Consistent design/look and feel throughout the website – ie. Images that come from the same “family”;
• Images – each page needs to have more interest than simply text – we envisage ”Reiki” related images on each page – See “Images” below.
• Premium – the design needs to be clean and information easily readable
• Simple and clear navigation

Functionality
Note we need to be able to edit and update the finished web site - Coding Required
• Simple content management system that we can easily update ourselves after website is complete
• Need the website address to match the url

Design References:
Looking for a nice simple to navigate website.
Below are some references to existing web sites that we quite like:

http://www.marthavale.com.au/construction/
This one looks and feels professional

http://www.brookfieldgardens.com.au/
This one feels very clean

http://www.tallpinesyards.com.au/products
This one as it looks clean and smart
 

Examples of Images for each page:
Please note that I do not want to use any photos of people receiving treatments who are not wearing clothes or who are wearing towels, as this is not the service i am providing. All my treatments will be fully clothed so I do not want to give the impression that they will have to remove any clothing. Thank you

Examples of “Reiki” related images that we quite like are:
• http://www.pictarvault.com/stock-illustration-40918276-chakra-and-meditation.php?st=5190642
• http://www.pictarvault.com/stock-illustration-6127403-healing-hands.php?st=5190642

SEO – organic search only
• We require advise as to how best optimise the website for organic search
o Linking to other websites
o Zentara +
o Zentara map of location?
o Update of content frequently?

Review
We would like to have the ability to review a draft of the web site design prior to finalisation.

WEB SITE CONTENT

- Please see attached file 'Detailed Layout Of Website and Content.
- Please include logo on home page.
- Please follow home page menu options as shown
- Please include all text and images provided
Updates

hi thanks for all your designs so far, i just want to make it clear that i don't want to use any photos where the client is having a treatment with no clothes on. This is not the treatments i will be giving so i don't want to give the wrong impression. As it states in the brief i want to use my logo provided (tree) and image/s of nature for the homepage and have a clear navigation menu to the different sections. Please include my picture in the about section; also include the picture of the healing room provided, as well as other images similar to the examples provided. 

Thank you

Target Market(s)

People who are looking for 'alternative' healing methods.
People interested in reiki for relaxation purposes.
People who have tried conventional medicines and have not been able to be cured/healed.
People of all ages.

Industry/Entity Type

Business

Requirements
Must have
• Please see 'design breif" and 'web content" above.
Codding required - Must be able to easily edit and modify and update after site is complete.
Nice to have
• Pictures of nature example waterfall on home page
Should not have
• Pictures of people receiving treatments with no clothes or wearing towels. As all treatments will be fully clothed and i don't want to give the idea that you must remove any clothing.

```html
<!DOCTYPE html>
<html lang="en">
<head>
<meta charset="utf-8">
<title>Still Meadow Energy Healing</title>
<link href="https://fonts.googleapis.com/css2?family=Signika:wght@300;400;600&family=Arimo:wght@400;700&display=swap" rel="stylesheet">
<style>
  :root{
    --green:#7fb51f;
    --green-dark:#5f8f12;
    --green-line:#9cc43a;
    --ink:#2b2b2b;
    --text:#5a5a5a;
    --page:#f1f1f1;
    --white:#fff;
    --hero-edge:#5d7a2c;
    --hero-mid:#8aa450;
    --hero-light:#b3c386;
    --foot-a:#3b3c3e;
    --foot-b:#1c1d1f;
    --bar:#dcdcdc;
  }
  *{margin:0;padding:0;box-sizing:border-box}
  html,body{width:764px;height:1200px;overflow:hidden}
  body{position:relative;background:var(--page);font-family:"Arimo",Arial,sans-serif;color:var(--text)}
  .abs{position:absolute}

  /* header */
  .site-header{left:0;top:0;width:764px;height:61px;background:var(--white)}
  .brand{left:139px;top:15px;display:flex;align-items:center;gap:8px}
  .brand-dot{width:28px;height:28px;border-radius:50%;background:var(--green-dark)}
  .brand-name{font:700 10px/1.15 "Arimo",Arial,sans-serif;color:var(--ink);width:110px}
  .nav{left:311px;top:16px;width:320px;height:24px}
  .nav-home{position:absolute;left:0;top:0;width:24px;height:24px;border-radius:3px;background:var(--green);display:flex;align-items:center;justify-content:center;box-shadow:inset 0 -2px 0 rgba(0,0,0,.12)}
  .nav a{font:700 10.5px "Arimo",Arial,sans-serif;color:#555;text-decoration:none;position:absolute;top:7px;white-space:nowrap}

  /* hero */
  .hero{left:0;top:61px;width:764px;height:212px;
    background:
      radial-gradient(ellipse 60% 80% at 35% 35%,rgba(200,212,160,.75),rgba(200,212,160,0) 70%),
      linear-gradient(90deg,var(--hero-edge),var(--hero-mid) 30%,var(--hero-light) 50%,var(--hero-mid) 72%,var(--hero-edge));}
  .hero-shade{left:0;top:61px;width:764px;height:212px;background:linear-gradient(rgba(0,0,0,0) 60%,rgba(40,60,15,.35))}
  .hero-title{left:210px;top:72px;font:300 38px "Signika",sans-serif;color:var(--white);text-shadow:0 1px 3px rgba(0,0,0,.25)}
  .hero-caption{left:147px;top:123px;width:197px;height:48px;background:rgba(60,80,30,.55);color:var(--white);font-size:8px;line-height:11px;padding:6px 10px}
  .hero-visual{left:344px;top:69px;width:273px;height:176px;
    background:
      radial-gradient(circle at 50% 60%,#e3ecd2 0,#e3ecd2 22%,rgba(227,236,210,0) 45%),
      radial-gradient(circle at 82% 20%,#e6d2ef 0,rgba(230,210,239,0) 28%),
      radial-gradient(circle at 15% 25%,#f3dbe8 0,rgba(243,219,232,0) 25%),
      radial-gradient(circle at 85% 80%,#f6dccd 0,rgba(246,220,205,0) 25%),
      radial-gradient(circle at 15% 78%,#d8e7f3 0,rgba(216,231,243,0) 25%),
      #fff;
    box-shadow:0 2px 6px rgba(0,0,0,.2)}
  .read-more{left:323px;top:167px;width:80px;height:80px;border-radius:50%;background:radial-gradient(circle at 50% 35%,#8fc22c,#5f9210);border:5px solid #a5cf4c;color:var(--white);font:700 9px "Arimo",sans-serif;text-align:center;padding-top:18px;box-shadow:0 3px 8px rgba(0,0,0,.35)}
  .read-more .plus{display:block;font:300 24px/22px "Arimo",sans-serif}
  .hero-arrow{top:147px;width:24px;height:46px;background:rgba(255,255,255,.25);border-radius:3px;display:flex;align-items:center;justify-content:center}
  .hero-dots{left:170px;top:244px;display:flex;gap:6px}
  .hero-dots span{width:8px;height:8px;border-radius:50%;background:rgba(255,255,255,.45)}
  .hero-dots span.on{background:var(--white)}

  /* articles */
  .article-title{left:129px;font:300 24px "Signika",sans-serif;color:var(--ink)}
  .rule{left:129px;width:504px;height:2px;background:var(--green-line)}
  .meta{left:129px;width:504px;font-size:7.5px;color:#777;display:flex;justify-content:space-between;align-items:center}
  .meta span{display:flex;align-items:center;gap:3px}
  .meta b{color:var(--green-dark);font-weight:400}
  .meta .tools{color:var(--green-dark);gap:4px}
  .thumb{left:129px;width:160px}
  .copy{left:295px;width:338px;font-size:7.5px;line-height:11px;color:var(--text)}
  .copy p{margin-bottom:8px}
  .bullets{font-size:7.5px;line-height:10.5px;color:var(--text);list-style:disc;padding-left:10px}

  .thumb-svh{background:
      radial-gradient(ellipse 55% 40% at 45% 55%,#e8cbb2,rgba(232,203,178,0) 70%),
      linear-gradient(160deg,#3e2a20 0,#6b4a36 30%,#c9a78c 60%,#f1ece6 100%)}
  .thumb-reiki{background:
      radial-gradient(ellipse 50% 45% at 55% 50%,#e7c2a6,rgba(231,194,166,0) 70%),
      linear-gradient(135deg,#f4eee8 0,#d9b49a 45%,#8c5e45 80%,#5a3a2a)}
  .thumb-chakra{background:
      radial-gradient(ellipse 20% 45% at 35% 50%,#d9dde8,rgba(217,221,232,0) 75%),
      #fff;border:1px solid #e1e1e1}

  /* footer links bar */
  .link-bar{left:129px;top:960px;width:504px;height:29px;background:linear-gradient(#e6e6e6,#d6d6d6);border-radius:6px;border:1px solid #c8c8c8;display:flex;align-items:center;gap:12px;padding-left:8px;font:700 8px "Arimo",sans-serif;color:#333;z-index:2}

  /* footer */
  .site-footer{left:0;top:975px;width:764px;height:225px;background:linear-gradient(var(--foot-a),var(--foot-b))}
  .foot-head{top:1004px;font:400 13px "Signika",sans-serif;color:var(--white)}
  .foot-rule{top:1027px;width:157px;height:2px;background:var(--green-line)}
  .portrait{left:137px;top:1048px;width:152px;height:107px;
    background:
      radial-gradient(ellipse 28% 42% at 52% 48%,#c79a7c,rgba(199,154,124,0) 75%),
      radial-gradient(ellipse 45% 35% at 50% 100%,#151515,rgba(21,21,21,0) 80%),
      linear-gradient(135deg,#2f4a1c,#5d7f38 40%,#3a5a22 70%,#1f3013)}
  .map{left:309px;top:1048px;width:154px;height:107px;
    background:
      radial-gradient(circle at 38% 42%,#b9cfa3 0,rgba(185,207,163,0) 22%),
      radial-gradient(circle at 78% 70%,#cfdcc0 0,rgba(207,220,192,0) 25%),
      linear-gradient(135deg,#efeee8,#e4e6df);
    border:2px solid #fff}
  .contact-row{left:487px;display:flex;gap:6px;font-size:7.5px;line-height:10px;color:var(--white)}
  .contact-row .green{color:var(--green);font-weight:700}
  .to-top{left:357px;top:1184px;width:50px;height:16px;background:var(--white);border-radius:4px 4px 0 0;font-size:7px;color:#333;text-align:center;padding-top:3px}
</style>
</head>
<body>

<header class="site-header abs">
  <div class="brand abs"><span class="brand-dot"></span><span class="brand-name">STILL MEADOW ENERGY HEALING</span></div>
  <nav class="nav abs">
    <span class="nav-home"><svg width="12" height="11" viewBox="0 0 12 11"><path d="M6 0L0 5h2v6h3V7h2v4h3V5h2z" fill="#fff"/></svg></span>
    <a style="left:33px">Treatments</a>
    <a style="left:97px">About</a>
    <a style="left:141px">Faq's</a>
    <a style="left:181px">Contact Us</a>
    <a style="left:244px">Testimonials</a>
  </nav>
</header>

<section class="hero abs"></section>
<div class="hero-shade abs"></div>
<h1 class="hero-title abs">SHV</h1>
<div class="hero-caption abs">SVH is a healing technique that allows the healer to create unique and specific healing plans for individual clients which…</div>
<div class="hero-visual abs" role="img" aria-label="Illustration of a meditating figure surrounded by coloured chakra symbols"></div>
<div class="read-more abs"><span class="plus">+</span>Read More</div>
<div class="hero-arrow abs" style="left:111px"><svg width="10" height="16"><path d="M8 2L2 8l6 6" stroke="#fff" stroke-width="2.5" fill="none"/></svg></div>
<div class="hero-arrow abs" style="left:628px"><svg width="10" height="16"><path d="M2 2l6 6-6 6" stroke="#fff" stroke-width="2.5" fill="none"/></svg></div>
<div class="hero-dots abs"><span></span><span class="on"></span><span></span></div>

<h2 class="article-title abs" style="top:286px">Serenity Vibration Healing (SVH)</h2>
<div class="rule abs" style="top:319px"></div>
<div class="meta abs" style="top:334px">
  <span><svg width="7" height="7"><rect x=".5" y=".5" width="6" height="6" fill="none" stroke="#888"/></svg>Category: <b>Treatments</b></span>
  <span class="tools"><svg width="8" height="7"><rect x="0" y="2" width="8" height="4" fill="#5f8f12"/><rect x="2" y="0" width="4" height="3" fill="#5f8f12"/></svg>Print&nbsp;<svg width="8" height="6"><rect x=".5" y=".5" width="7" height="5" fill="none" stroke="#5f8f12"/><path d="M.5 .5l3.5 3 3.5-3" fill="none" stroke="#5f8f12"/></svg>Email</span>
</div>
<div class="thumb thumb-svh abs" style="top:352px;height:109px" role="img" aria-label="Photo of a client resting peacefully during a healing session"></div>
<div class="copy abs" style="top:354px">
  <p>SVH is a healing technique that allows the healer to create unique and specific healing plans for individual clients which are then implemented by the Creator. It is an extremely powerful healing method that allows you to release limiting, beliefs perceptions and any negative or blocked energy that may have built up over the course of one's life. It frees the mind from unnecessary, distracting thoughts that inhibit focus and clarity.</p>
  <p>SVH is a safe and effective way to restore harmony and balance to the body and mind for lasting change. Any issue can be addressed including:</p>
  <ul class="bullets" style="list-style:none;padding-left:0"><li>Physical and mental health</li><li>Personal relationships</li></ul>
</div>
<ul class="bullets abs" style="left:133px;top:472px">
  <li>Issues related to work</li><li>Grief and loss</li><li>Past traumatic experiences</li>
  <li>Irrational fears and phobias</li><li>Curses and Spells</li><li>Past life and Karmic Issues</li>
</ul>

<h2 class="article-title abs" style="top:554px">Reiki</h2>
<div class="rule abs" style="top:587px"></div>
<div class="meta abs" style="top:603px">
  <span><svg width="7" height="7"><rect x=".5" y=".5" width="6" height="6" fill="none" stroke="#888"/></svg>Category: <b>Treatments</b></span>
  <span class="tools"><svg width="8" height="7"><rect x="0" y="2" width="8" height="4" fill="#5f8f12"/><rect x="2" y="0" width="4" height="3" fill="#5f8f12"/></svg>Print&nbsp;<svg width="8" height="6"><rect x=".5" y=".5" width="7" height="5" fill="none" stroke="#5f8f12"/><path d="M.5 .5l3.5 3 3.5-3" fill="none" stroke="#5f8f12"/></svg>Email</span>
</div>
<div class="thumb thumb-reiki abs" style="top:621px;height:111px" role="img" aria-label="Photo of hands giving a gentle reiki treatment"></div>
<div class="copy abs" style="top:620px">
  <p>The Japanese name Reiki translates in English to "universal life force energy." The living body radiates warmth and energy and this energy is the life force itself</p>
  <p>It is a method of natural healing that uses the energy channelled through a practitioner's hands to remove the obstructions that prevent the healing of the mind and body.</p>
  <p>Founded in Japan by Kenji Arata in the later part of the 19th century, the method has flourished, being handed down from master to student to the present day.</p>
  <p>Reiki is not a religion - it is a healing technique. It does not any require religious belief nor does it require the surrender or modification of any beliefs the individual may have.</p>
</div>

<h2 class="article-title abs" style="top:756px">What is a Chakra?</h2>
<div class="rule abs" style="top:790px"></div>
<div class="meta abs" style="top:806px">
  <span><svg width="7" height="7"><rect x=".5" y=".5" width="6" height="6" fill="none" stroke="#888"/></svg>Category: <b>FAQ</b></span>
  <span class="tools"><svg width="8" height="7"><rect x="0" y="2" width="8" height="4" fill="#5f8f12"/><rect x="2" y="0" width="4" height="3" fill="#5f8f12"/></svg>Print&nbsp;<svg width="8" height="6"><rect x=".5" y=".5" width="7" height="5" fill="none" stroke="#5f8f12"/><path d="M.5 .5l3.5 3 3.5-3" fill="none" stroke="#5f8f12"/></svg>Email</span>
</div>
<div class="thumb thumb-chakra abs" style="top:824px;height:109px" role="img" aria-label="Diagram of a seated figure with the seven chakras labelled"></div>
<div class="copy abs" style="top:823px">
  <p>The word chakra means 'spinning wheel or disc of energy'. The human body has seven major chakras. They are located from the base of the spine to the crown of the head. These energy centres are associated with different elements, organs, functions and emotions. When one or more chakra is blocked it has a major effect on the flow of energy within the body, leading to imbalance.</p>
</div>

<footer class="site-footer abs"></footer>
<nav class="link-bar abs"><span>Reiki</span><span>Serenity Vibration Healing</span><span>Privacy Policy</span></nav>
<h3 class="foot-head abs" style="left:133px">Rowan Hale</h3>
<h3 class="foot-head abs" style="left:305px">Location</h3>
<h3 class="foot-head abs" style="left:476px">Contact Details</h3>
<div class="foot-rule abs" style="left:129px"></div>
<div class="foot-rule abs" style="left:301px"></div>
<div class="foot-rule abs" style="left:473px"></div>
<div class="portrait abs" role="img" aria-label="Portrait photo of the healer standing among green foliage"></div>
<div class="map abs" role="img" aria-label="Street map showing the clinic location"></div>

<div class="contact-row abs" style="top:1050px">
  <svg width="8" height="10" viewBox="0 0 8 10"><rect x="1" y="0" width="6" height="10" rx="1" fill="#fff"/><rect x="2" y="1.5" width="4" height="6" fill="#222"/></svg>
  <span class="green">02 8555 0147</span>
</div>
<div class="contact-row abs" style="top:1075px">
  <svg width="8" height="10" viewBox="0 0 8 10"><path d="M4 0a3.5 3.5 0 0 0-3.5 3.5C.5 6 4 10 4 10s3.5-4 3.5-6.5A3.5 3.5 0 0 0 4 0z" fill="#fff"/><circle cx="4" cy="3.5" r="1.3" fill="#222"/></svg>
  <span><b>Still Meadow Energy Healing</b><br>14 Willow Crest Rd<br>Larkwood 2081<br>Australia</span>
</div>
<div class="contact-row abs" style="top:1129px">
  <svg width="10" height="8" viewBox="0 0 10 8"><rect width="10" height="8" fill="#fff"/><path d="M0 0l5 4 5-4" stroke="#222" fill="none"/></svg>
  <span class="green">rowan@stillmeadow.com.au</span>
</div>
<div class="to-top abs">Top ⌃</div>

</body>
</html>
```